E-Book for Independent Filmmakers. Looking for a simple design with a Human Figure, gazing at the sky, and a Shooting Star in background. Bonus Points if there's a Cinema camera on a tripod next to him. Current placeholder cover attached
(I don't own photo).

Target Market(s)

18 - 42

Industry/Entity Type

Film Production

Font styles to use
Sans Serif

Colors
1b1b1b
5c5c5c
b1b1b1

Requirements
Must have
• Simplicity, Elegance.
• LEAP PAST THE HORIZON
Nice to have
• Would be Awesome to experiment with 2 Designs, under Title "LEAP PAST THE HORIZON:"
• Subtitle Option 1: The 7 Layers of Modern Moviecraft
• Subtitle Option2: An eBook for Filmmakers
Should not have
• Boringness

```html
<!DOCTYPE html>
<html lang="en">
<head>
<meta charset="utf-8">
<title>Leap Past the Horizon — eBook Cover</title>
<link rel="stylesheet" href="https://fonts.googleapis.com/css2?family=League+Spartan:wght@700&family=Josefin+Sans:wght@300&display=swap">
<style>
  :root {
    --sky-deep: #0b2236;
    --sky-mid: #1f4a63;
    --sky-glow: #3d7388;
    --streak-violet: #4a4fc4;
    --title-white: #ffffff;
  }
  html, body {
    margin: 0;
    padding: 0;
    width: 1200px;
    height: 923px;
    overflow: hidden;
    background: var(--sky-deep);
  }
  .cover {
    position: relative;
    width: 1200px;
    height: 923px;
    overflow: hidden;
  }
  .cover__sky {
    position: absolute;
    inset: 0;
    background:
      radial-gradient(ellipse 45% 30% at 20% 35%, rgba(74,79,196,0.35) 0%, rgba(74,79,196,0) 70%),
      radial-gradient(ellipse 70% 60% at 60% 50%, var(--sky-glow) 0%, rgba(61,115,136,0) 72%),
      linear-gradient(160deg, var(--sky-deep) 0%, var(--sky-mid) 55%, var(--sky-deep) 100%);
  }
  .cover__title {
    margin: 0;
  }
  .title-line {
    position: absolute;
    left: 0;
    width: 1200px;
    text-align: center;
    white-space: nowrap;
    font-family: "League Spartan", sans-serif;
    font-weight: 700;
    line-height: 1;
    color: var(--title-white);
  }
  .title-line--leap { top: -5px; font-size: 373px; letter-spacing: 0.01em; }
  .title-line--past { top: 292px; font-size: 201px; letter-spacing: 0.01em; }
  .title-line--horizon { top: 487px; font-size: 236px; letter-spacing: -0.01em; }
  .subtitle {
    position: absolute;
    left: 0;
    top: 758px;
    width: 1200px;
    margin: 0;
    text-align: center;
    font-family: "Josefin Sans", sans-serif;
    font-weight: 300;
    font-size: 54px;
    line-height: 66px;
    letter-spacing: 0.28em;
    color: var(--title-white);
    text-transform: uppercase;
  }
  .subtitle span { display: block; }
</style>
</head>
<body>
  <main class="cover">
    <div class="cover__sky" role="img" aria-label="Night sky full of stars with violet shooting stars streaking across"></div>
    <h1 class="cover__title">
      <span class="title-line title-line--leap">LEAP</span>
      <span class="title-line title-line--past">PAST THE</span>
      <span class="title-line title-line--horizon">HORIZON</span>
    </h1>
    <p class="subtitle">
      <span>The 7 Layers of</span>
      <span>Modern Moviecraft</span>
    </p>
  </main>
</body>
</html>
```